Door Hanger Design for Electricians Serving Homes

I would like our logo incorporated into the door hanger. We would like a place for a tear off section on the bottom of the hanger with our contact information: K&T Electric - (555) 318-4702 - www.kandtelectric.example - info@kandtelectric.example.
Door Hanger Script
Front Side of the Door Hanger:
[Company Logo]
Need a Reliable Electrician?
Your Local Electrical Expert is Just Around the Corner!
• Quick Response Times
• Affordable Rates
• Quality Workmanship
• Fully Licensed & Insured
• Special Offer:
• 10% OFF Your First Service Call!
Back Side of the Door Hanger:
Don't Let Electrical Issues Keep You in the Dark!
From flickering lights to complete system upgrades, we've got all your
residential electrical needs covered. Our services include:
• Electrical Repairs & Troubleshooting
• Lighting Installation & Upgrades
• Safety Inspections & Code Compliance
• Energy-Efficient Solutions
• 24/7 Emergency Services
• Why Choose Us?
• Friendly, Local Service
• Over 30 Years of Experience
• Satisfaction Guaranteed
• Upfront Pricing
Call Us Today: [Your Phone Number]
Visit Our Website: [Your Website]
Book Your Appointment Now and Claim Your 10% Discount!
Offer valid for new customers on the first visit only. Mention this door hanger when
booking.
[Your Company Name and Contact Information]
Follow Us on Social Media for More Tips and Special Offers!
[Icons for social media platforms: Chatterpage, Pixmosaic, Quibbler, etc.]
Design Tips:
Use bold, clear fonts for easy reading.
Incorporate your brand colors and logo for instant recognition.
Include a clear call to action (CTA) on both sides.
Add a tear-off section at the bottom with your contact information for
convenience.
Use high-quality images or graphics related to electrical work to catch
the eye.
This door hanger design and copy aim to attract residential clients by
highlighting the benefits of your electrical services, special offers, and
how they can easily get in touch with you for their electrical needs.
The door knocker template will have three of the same design on front and three of the same design on the back. This template is from the print shop.

```html
<!DOCTYPE html>
<html lang="en">
<head>
<meta charset="utf-8">
<title>K&amp;T Electric Door Hanger</title>
<link href="https://fonts.googleapis.com/css2?family=Poppins:wght@300;400;500;600;700;800&family=Nunito:wght@900&family=Roboto:wght@400&display=swap" rel="stylesheet">
<style>
  :root{
    --red:#dc1f26;
    --black:#0c0c0c;
    --white:#ffffff;
    --backdrop:#bbbec1;
    --ink:#111111;
    --rule:#2a2a2a;
  }
  html,body{margin:0;padding:0;width:1200px;height:1200px;overflow:hidden;background:var(--backdrop);}
  .stage{position:absolute;left:0;top:0;width:1932px;height:1932px;transform:scale(0.621118);transform-origin:0 0;}
  .hanger{position:absolute;top:138px;width:711px;height:1655px;background:var(--white);overflow:hidden;box-shadow:2px 3px 6px rgba(0,0,0,.35);font-family:"Poppins",sans-serif;}
  .hanger--front{left:211px;}
  .hanger--back{left:976px;}
  .hanger__art{position:absolute;left:0;top:0;width:711px;height:1655px;}
  .brand{position:absolute;top:0;width:206px;height:235px;display:flex;flex-direction:column;align-items:center;justify-content:center;padding-bottom:30px;box-sizing:border-box;color:var(--black);font-family:"Poppins",sans-serif;font-weight:700;line-height:1;}
  .brand__mark{font-size:64px;letter-spacing:-1px;}
  .brand__sub{font-size:21px;margin-top:10px;letter-spacing:1px;}
  .front .brand{left:475px;}
  .back .brand{left:22px;}

  .headline{position:absolute;left:0;width:711px;text-align:center;font-weight:800;line-height:1;letter-spacing:-1px;white-space:nowrap;}
  .headline--red{top:582px;font-size:74px;color:var(--red);}
  .headline--black{top:646px;font-size:88px;color:var(--ink);}
  .tagline{position:absolute;left:43px;top:740px;width:625px;height:97px;background:var(--red);border-radius:10px;color:var(--white);font-size:36px;line-height:45px;text-align:center;display:flex;align-items:center;justify-content:center;font-weight:400;}
  .benefits{position:absolute;left:58px;top:868px;margin:0;padding:0;list-style:none;}
  .benefits li{display:flex;align-items:center;height:66px;font-size:45px;color:var(--ink);white-space:nowrap;}
  .benefits svg{width:40px;height:40px;margin-right:22px;flex:none;}

  .offer-pct{position:absolute;left:43px;top:1158px;width:625px;text-align:center;color:var(--white);font-weight:700;font-size:116px;line-height:1;letter-spacing:-2px;}
  .offer-pct span{color:var(--red);}
  .offer-sub{position:absolute;left:43px;top:1313px;width:625px;text-align:center;color:var(--white);font-family:"Nunito",sans-serif;font-weight:900;font-size:40px;line-height:48px;white-space:nowrap;}

  .cta-tab{position:absolute;left:204px;width:303px;text-align:center;font-family:"Nunito",sans-serif;font-weight:900;font-size:34px;line-height:1;white-space:nowrap;}
  .front .cta-tab{top:1381px;color:var(--black);}
  .back .cta-tab{top:1384px;color:var(--white);}
  .phone{position:absolute;top:1440px;color:var(--white);font-weight:700;font-size:67px;line-height:90px;letter-spacing:-1px;white-space:nowrap;}
  .front .phone{left:148px;}
  .back .phone{left:154px;font-size:68px;}
  .site-pill{position:absolute;left:204px;top:1540px;width:303px;height:44px;border-radius:22px;background:var(--red);border:2px solid var(--black);box-sizing:border-box;color:var(--white);font-size:31px;line-height:40px;text-align:center;white-space:nowrap;}
  .site-url{position:absolute;top:1596px;font-size:35px;line-height:46px;color:var(--ink);display:flex;align-items:center;white-space:nowrap;}
  .site-url svg{width:28px;height:28px;margin-right:8px;}
  .front .site-url{left:116px;}
  .back .site-url{left:115px;}

  .back-headline{position:absolute;left:0;top:486px;width:711px;text-align:center;color:var(--white);font-family:"Nunito",sans-serif;font-weight:900;font-size:49px;line-height:54px;}
  .intro{position:absolute;left:30px;top:614px;width:650px;height:150px;background:var(--black);border-radius:22px;color:var(--white);font-size:30px;line-height:41px;text-align:center;display:flex;align-items:center;justify-content:center;}
  .services{position:absolute;left:56px;top:789px;width:611px;margin:0;padding:0;list-style:none;font-family:"Roboto",sans-serif;}
  .services li{height:54px;border-bottom:2px solid var(--rule);text-align:center;font-size:33px;line-height:56px;color:var(--ink);margin-bottom:1.2px;white-space:nowrap;}
  .services li:last-child{border-bottom:none;}
</style>
</head>
<body>
<div class="stage">

  <section class="hanger hanger--front front">
    <svg class="hanger__art" viewBox="0 0 711 1655">
      <defs>
        <linearGradient id="cityNight" x1="0" y1="0" x2="0" y2="1">
          <stop offset="0" stop-color="#3f73c4"/>
          <stop offset=".5" stop-color="#3a5c9c"/>
          <stop offset="1" stop-color="#4b4652"/>
        </linearGradient>
        <linearGradient id="footFront" x1="0" y1="0" x2="1" y2="1">
          <stop offset="0" stop-color="#000"/>
          <stop offset=".5" stop-color="#3a3a3a"/>
          <stop offset="1" stop-color="#050505"/>
        </linearGradient>
      </defs>
      <polygon points="0,0 711,0 711,462 0,557" fill="url(#cityNight)" role="img" aria-label="City skyline at dusk with lit office towers"/>
      <polygon points="0,557 711,462 711,497 0,562" fill="var(--red)"/>
      <polygon points="8,568 711,503 711,557 622,531" fill="var(--black)"/>
      <line x1="134" y1="-10" x2="300" y2="150" stroke="var(--backdrop)" stroke-width="14"/>
      <circle cx="356" cy="220" r="100" fill="var(--backdrop)"/>
      <path d="M475,0 H681 V205 L578,235 L475,205 Z" fill="var(--white)"/>
      <rect x="0" y="1317" width="711" height="248" fill="url(#footFront)"/>
      <rect x="43" y="1152" width="625" height="222" rx="12" fill="var(--black)"/>
      <path d="M43,1270 L356,1304 L668,1270 V1362 Q668,1374 656,1374 H55 Q43,1374 43,1362 Z" fill="var(--red)"/>
      <rect x="50" y="1159" width="611" height="208" rx="8" fill="none" stroke="var(--white)" stroke-width="2" stroke-dasharray="6 5"/>
      <path d="M622,1159 H661 V1198 Z" fill="#e4e4e4"/>
      <path d="M622,1159 L661,1198 L628,1190 Z" fill="#9a9a9a"/>
      <path d="M204,1374 H507 V1420 Q507,1430 497,1430 H366 L356,1436 L346,1430 H214 Q204,1430 204,1420 Z" fill="var(--white)"/>
      <circle cx="95" cy="1484" r="36" fill="var(--white)"/>
      <circle cx="95" cy="1484" r="31" fill="var(--red)"/>
      <path d="M80,1468 l8,-3 6,12 -5,4 q4,9 12,13 l5,-5 12,6 -3,8 q-14,3 -28,-12 q-12,-13 -7,-23 z" fill="var(--black)"/>
    </svg>

    <div class="brand"><div class="brand__mark">K&amp;T</div><div class="brand__sub">ELECTRIC, LLC</div></div>

    <div class="headline headline--red">NEED A RELIABLE</div>
    <div class="headline headline--black">ELECTRICIAN?</div>
    <div class="tagline">Your Local Electrical Expert is<br>Just Around the Corner!</div>

    <ul class="benefits">
      <li><svg viewBox="0 0 40 40"><circle cx="20" cy="20" r="19" fill="#dc1f26"/><path d="M11,20 l6,6 12,-12" fill="none" stroke="#fff" stroke-width="5" stroke-linecap="round" stroke-linejoin="round"/></svg>Quick Response Times</li>
      <li><svg viewBox="0 0 40 40"><circle cx="20" cy="20" r="19" fill="#dc1f26"/><path d="M11,20 l6,6 12,-12" fill="none" stroke="#fff" stroke-width="5" stroke-linecap="round" stroke-linejoin="round"/></svg>Affordable Rates</li>
      <li><svg viewBox="0 0 40 40"><circle cx="20" cy="20" r="19" fill="#dc1f26"/><path d="M11,20 l6,6 12,-12" fill="none" stroke="#fff" stroke-width="5" stroke-linecap="round" stroke-linejoin="round"/></svg>Quality Workmanship</li>
      <li><svg viewBox="0 0 40 40"><circle cx="20" cy="20" r="19" fill="#dc1f26"/><path d="M11,20 l6,6 12,-12" fill="none" stroke="#fff" stroke-width="5" stroke-linecap="round" stroke-linejoin="round"/></svg>Fully Licensed &amp; Insured</li>
    </ul>

    <div class="offer-pct">10<span>%</span> OFF</div>
    <div class="offer-sub">YOUR FIRST SERVICE CALL!</div>

    <div class="cta-tab">CALL US TODAY</div>
    <div class="phone">(555) 318-4702</div>
    <div class="site-pill">Visit Our Website</div>
    <div class="site-url"><svg viewBox="0 0 28 28"><g fill="none" stroke="#dc1f26" stroke-width="2"><circle cx="14" cy="14" r="12"/><ellipse cx="14" cy="14" rx="5" ry="12"/><line x1="2" y1="14" x2="26" y2="14"/><line x1="4" y1="8" x2="24" y2="8"/><line x1="4" y1="20" x2="24" y2="20"/></g></svg>www.kandtelectric.example</div>
  </section>

  <section class="hanger hanger--back back">
    <svg class="hanger__art" viewBox="0 0 711 1655">
      <defs>
        <radialGradient id="bulbGlow" cx=".7" cy=".6" r=".7">
          <stop offset="0" stop-color="#f3a63a"/>
          <stop offset=".35" stop-color="#8a4a14"/>
          <stop offset=".75" stop-color="#2a160a"/>
          <stop offset="1" stop-color="#0d0805"/>
        </radialGradient>
        <linearGradient id="footBack" x1="0" y1="0" x2="1" y2="1">
          <stop offset="0" stop-color="#000"/>
          <stop offset=".5" stop-color="#3a3a3a"/>
          <stop offset="1" stop-color="#050505"/>
        </linearGradient>
      </defs>
      <polygon points="0,0 711,0 711,472 0,355" fill="url(#bulbGlow)" role="img" aria-label="Glowing vintage filament light bulbs against a dark background"/>
      <polygon points="0,366 711,476 711,484 0,400" fill="var(--red)"/>
      <polygon points="0,400 711,484 711,486 100,435 0,465" fill="var(--black)"/>
      <polygon points="0,465 100,435 711,486 711,680 0,680" fill="var(--red)"/>
      <line x1="550" y1="-10" x2="420" y2="118" stroke="var(--backdrop)" stroke-width="14"/>
      <circle cx="354" cy="220" r="100" fill="var(--backdrop)"/>
      <path d="M22,0 H228 V205 L125,235 L22,205 Z" fill="var(--white)"/>
      <rect x="0" y="1379" width="711" height="186" fill="url(#footBack)"/>
      <path d="M214,1364 H497 L507,1372 V1427 Q507,1437 497,1437 H366 L356,1443 L346,1437 H214 Q204,1437 204,1427 V1372 Z" fill="var(--red)"/>
      <circle cx="87" cy="1484" r="43" fill="var(--white)"/>
      <circle cx="87" cy="1484" r="38" fill="var(--red)"/>
      <path d="M70,1466 l9,-3 7,13 -6,5 q4,10 13,14 l6,-6 13,7 -3,9 q-16,3 -31,-13 q-13,-15 -8,-26 z" fill="var(--black)"/>
    </svg>

    <div class="brand"><div class="brand__mark">K&amp;T</div><div class="brand__sub">ELECTRIC, LLC</div></div>

    <div class="back-headline">Don't Let Electrical Issues<br>Keep You in the Dark!</div>
    <div class="intro">From flickering lights to complete<br>system upgrades, we've got all your<br>residential electrical needs covered.</div>

    <ul class="services">
      <li>Electrical Repairs &amp; Troubleshooting</li>
      <li>Lighting Installation &amp; Upgrades</li>
      <li>Safety Inspections &amp; Code Compliance</li>
      <li>Energy-Efficient Solutions</li>
      <li>24/7 Emergency Services</li>
      <li>Why Choose Us?</li>
      <li>Friendly, Local Service</li>
      <li>Over 30 Years of Experience</li>
      <li>Satisfaction Guaranteed</li>
      <li>Upfront Pricing</li>
    </ul>

    <div class="cta-tab">CALL US TODAY</div>
    <div class="phone">(555) 318-4702</div>
    <div class="site-pill">Visit Our Website</div>
    <div class="site-url"><svg viewBox="0 0 28 28"><g fill="none" stroke="#dc1f26" stroke-width="2"><circle cx="14" cy="14" r="12"/><ellipse cx="14" cy="14" rx="5" ry="12"/><line x1="2" y1="14" x2="26" y2="14"/><line x1="4" y1="8" x2="24" y2="8"/><line x1="4" y1="20" x2="24" y2="20"/></g></svg>www.kandtelectric.example</div>
  </section>

</div>
</body>
</html>
```